Cool Website Design Bright Peel Co.

We need a new website, using our existing domain, with a similar function to https://www.quilldecals.example/ or https://www.marlowfilmworks.example/ instagram bright_peel.co.
We can send google docs with pictures.
Logo attached

```html
<!DOCTYPE html>
<html lang="en">
<head>
<meta charset="utf-8">
<title>Bright Peel Co</title>
<link href="https://fonts.googleapis.com/css2?family=Oswald:wght@500;600&family=Poppins:wght@400;500;600&display=swap" rel="stylesheet">
<style>
:root{
  --black:#000;
  --ink:#0b0b0c;
  --panel:#2a2a2c;
  --panel-hi:#4a4a4d;
  --blue:#1c9cf2;
  --purple:#7a3fdc;
  --violet:#8a4be0;
  --text:#fff;
  --muted:#d6d6d6;
  --star:#f6b51c;
  --grad:linear-gradient(90deg,var(--blue),var(--purple));
}
*{margin:0;padding:0;box-sizing:border-box}
html,body{width:1200px;height:4000px;overflow:hidden;background:var(--black)}
body{position:relative;font-family:'Poppins',sans-serif;color:var(--text)}
.abs{position:absolute}
.heading{font-family:'Oswald',sans-serif;font-weight:600;text-transform:uppercase;letter-spacing:.5px}
.btn{position:absolute;display:flex;align-items:center;justify-content:center;font-family:'Oswald',sans-serif;font-weight:500;font-size:16px;text-transform:uppercase;color:#fff;background:var(--grad)}
.btn-blue{background:var(--blue)}
.wordmark{font-family:'Oswald',sans-serif;font-weight:600;color:var(--violet);text-transform:uppercase;display:flex;align-items:center;gap:8px}
.wordmark i{display:block;width:14px;height:14px;background:var(--violet)}

/* nav */
.nav{top:0;left:0;width:1200px;height:95px;background:var(--black)}
.nav a{position:absolute;top:38px;font-family:'Oswald',sans-serif;font-weight:500;font-size:14px;text-transform:uppercase;color:#fff;text-decoration:none}
.nav a.active{color:var(--violet)}
.nav .wordmark{position:absolute;left:600px;top:30px;transform:translateX(-50%);font-size:24px}

/* hero */
.hero{top:95px;left:0;width:1200px;height:627px;background:radial-gradient(ellipse at 45% 60%,#5a2a6e 0%,#2a1a36 35%,#241c22 60%,#1a1416 100%)}
.hero-title{top:290px;width:1200px;text-align:center;font-size:70px;line-height:1}
.hero-sub{top:368px;width:1200px;text-align:center;font-size:34px;line-height:40px}

/* about */
.about{top:722px;left:0;width:1200px;height:574px;background:var(--black)}
.frame-accent{left:75px;top:802px}
.about-photo{left:93px;top:825px;width:582px;height:389px;background:linear-gradient(120deg,#3a3a40 0%,#6a4030 45%,#d2571e 70%,#2a2a30 100%)}
.about h2{position:absolute;left:705px;top:830px;font-size:46px;line-height:52px}
.about h2 span{color:var(--blue)}
.about p{position:absolute;left:705px;top:937px;width:420px;font-size:15px;line-height:29px;color:var(--muted)}

/* services */
.services{top:1296px;left:0;width:1200px;height:663px;background:radial-gradient(ellipse at 50% 60%,#3a3a3e 0%,#1c1c1e 55%,#0e0e10 100%)}
.section-title{position:absolute;width:1200px;text-align:center;font-size:44px}
.svc{position:absolute;width:280px}
.svc h3{font-size:18px;font-weight:600;color:var(--blue);margin-bottom:6px}
.svc p{font-size:15px;line-height:24px;color:var(--muted)}
.svc.right{text-align:right}
.svc.center{text-align:center}
.icon{position:absolute;width:76px;height:76px;border-radius:50%;background:linear-gradient(135deg,var(--blue),var(--purple));display:flex;align-items:center;justify-content:center}
.car{left:365px;top:1607px;width:450px;height:256px;border-radius:48% 48% 30% 30%;background:radial-gradient(ellipse at 50% 55%,#7a80a8 0%,#4d5272 50%,#262838 80%,transparent 81%)}

/* reviews */
.reviews{top:1959px;left:0;width:1200px;height:501px;background:#0d0d0e}
.reviews h2{position:absolute;left:73px;top:2027px;font-size:44px}
.badge{left:925px;top:2021px;width:202px;height:62px;border-radius:10px;background:#1e1e20;border:1px solid #333}
.badge i{position:absolute;left:6px;top:6px;width:50px;height:50px;border-radius:50%;border:6px solid #34a853}
.card{position:absolute;top:2111px;width:328px;height:210px;border-radius:6px;background:var(--panel);padding:26px 16px}
.card.focus{background:var(--panel-hi)}
.avatar{position:absolute;left:18px;top:22px;width:46px;height:46px;border-radius:50%;background:#555;display:flex;align-items:center;justify-content:center;font-weight:600;font-size:20px}
.card h4{position:absolute;left:82px;top:24px;font-size:14px;font-weight:600;text-transform:uppercase}
.stars{position:absolute;left:82px;top:44px;color:var(--star);font-size:16px;letter-spacing:4px}
.card p{position:absolute;left:16px;top:83px;width:300px;font-size:13px;line-height:23px;color:var(--muted)}
.card time{position:absolute;left:19px;top:173px;font-size:12px;color:var(--blue)}
.arrow{position:absolute;top:2200px}

/* gallery */
.gallery{top:2460px;left:0;width:1200px;height:673px;background:linear-gradient(180deg,#0e0e0f,#1c1c1e)}
.shot{position:absolute;border-radius:8px}

/* contact */
.contact{top:3133px;left:0;width:1200px;height:567px;background:var(--black)}
.form-box{left:93px;top:3233px;width:582px;height:389px;background:var(--purple);padding:0 17px}
.form-box h2{position:absolute;left:17px;top:22px;font-size:44px}
.field{position:absolute;background:#fff;color:#333;font-size:12px;padding:14px 14px}
.contact-info h2{position:absolute;left:740px;top:3225px;font-size:44px}
.info{position:absolute;left:740px}
.info .dot{position:absolute;left:0;top:0;width:50px;height:50px;border-radius:50%;background:linear-gradient(135deg,var(--blue),var(--purple));display:flex;align-items:center;justify-content:center}
.info h5{position:absolute;left:75px;top:-8px;font-family:'Oswald',sans-serif;font-weight:500;font-size:16px;color:var(--blue);text-transform:uppercase;white-space:nowrap}
.info p{position:absolute;left:75px;top:16px;width:320px;font-size:15px;line-height:26px;color:var(--muted)}

/* footer */
.footer{top:3700px;left:0;width:1200px;height:300px;background:#111113}
.footer .wordmark{position:absolute;left:124px;top:3776px;font-size:28px}
.copy{position:absolute;left:70px;top:3890px;width:260px;text-align:center;font-size:13px;line-height:22px;color:var(--muted)}
.footer h6{position:absolute;top:3772px;font-family:'Oswald',sans-serif;font-weight:500;font-size:20px;text-transform:uppercase}
.flink{position:absolute;font-size:13px;color:var(--muted)}
.social{position:absolute;top:3821px;width:22px;height:22px;border-radius:50%;background:#fff}
</style>
</head>
<body>

<header class="abs nav">
  <a class="active" style="left:75px">Home</a>
  <a style="left:149px">About Us</a>
  <a style="left:248px">Services</a>
  <a style="left:345px">Gallery</a>
  <a style="left:438px">FAQ's</a>
  <div class="wordmark"><i></i>Bright Peel Co</div>
  <a style="left:708px">Products</a>
  <a style="left:812px">Blog</a>
  <a style="left:885px">Contact</a>
  <span class="btn" style="left:973px;top:23px;width:153px;height:48px;font-size:15px">Request a Quote</span>
</header>

<section class="abs hero" role="img" aria-label="Sports car with a bold multicolour wrap in a workshop"></section>
<h1 class="abs heading hero-title">Bright Peel Co</h1>
<p class="abs heading hero-sub">Custom designs, flawless installation,<br>and long-lasting protection.</p>
<span class="btn btn-blue" style="left:525px;top:466px;width:150px;height:44px">Request a Quote</span>

<section class="abs about">
</section>
<svg class="abs frame-accent" width="512" height="390" viewBox="0 0 512 390">
  <defs><linearGradient id="fa" x1="0" y1="0" x2="1" y2="0"><stop offset="0" stop-color="#7a3fdc"/><stop offset="1" stop-color="#1c9cf2"/></linearGradient></defs>
  <polygon points="0,0 512,0 478,22 18,22 18,368 0,388" fill="url(#fa)"/>
</svg>
<div class="abs about-photo" role="img" aria-label="Installer applying an orange and black wrap to a car door"></div>
<div class="about">
  <h2 class="heading">About <span>Bright</span><br><span>Peel Co</span></h2>
  <p>Sed ut perspiciatis unde omnis iste natus error sit voluptatem accusantium doloremque laudantium, totam rem aperiam, eaque ipsa quae ab illo inventore veritatis et quasi architecto beatae vitae dicta sunt explicabo. Nemo enim ipsam voluptatem quia voluptas sit aspernatur aut odit aut fugit, sed quia consequuntur magni dolores eos qui ratione.</p>
</div>
<span class="btn" style="left:705px;top:1158px;width:140px;height:46px">Read More</span>

<section class="abs services"></section>
<h2 class="section-title heading" style="top:1360px">Our Services</h2>
<div class="abs car" role="img" aria-label="Blue-grey estate car, front three-quarter view"></div>

<div class="svc center" style="left:460px;top:1440px"><h3>Vinyl Wraps</h3><p>Sed ut perspiciatis unde omnis iste natus error sit voluptatem.</p></div>
<div class="svc right" style="left:62px;top:1557px"><h3>Paint Protection Film</h3><p>Sed ut perspiciatis unde omnis iste natus error sit voluptatem.</p></div>
<div class="svc right" style="left:62px;top:1706px"><h3>Pro Detailing</h3><p>Sed ut perspiciatis unde omnis iste natus error sit voluptatem.</p></div>
<div class="svc" style="left:854px;top:1533px"><h3>Window Tinting</h3><p>Sed ut perspiciatis unde omnis iste natus error sit voluptatem.</p></div>
<div class="svc" style="left:854px;top:1706px"><h3>Ceramic Coating</h3><p>Sed ut perspiciatis unde omnis iste natus error sit voluptatem.</p></div>

<div class="icon" style="left:570px;top:1527px"><svg width="40" height="34" fill="none" stroke="#fff" stroke-width="2"><rect x="3" y="8" width="34" height="18" rx="4"/><circle cx="11" cy="28" r="3"/><circle cx="29" cy="28" r="3"/><path d="M9 8l4-6h14l4 6"/></svg></div>
<div class="icon" style="left:356px;top:1559px"><svg width="40" height="40" fill="none" stroke="#fff" stroke-width="2"><path d="M20 3l14 5v10c0 9-6 15-14 19C12 33 6 27 6 18V8z"/><path d="M13 20l5 5 9-10"/></svg></div>
<div class="icon" style="left:768px;top:1538px"><svg width="40" height="36" fill="none" stroke="#fff" stroke-width="2"><path d="M4 32V14L16 4h20v28z"/><path d="M4 20h32"/></svg></div>
<div class="icon" style="left:290px;top:1795px"><svg width="40" height="36" fill="none" stroke="#fff" stroke-width="2"><rect x="4" y="12" width="26" height="18" rx="3"/><path d="M30 18h6v10h-6"/><circle cx="12" cy="6" r="2"/><circle cx="20" cy="4" r="2"/></svg></div>
<div class="icon" style="left:844px;top:1802px"><svg width="40" height="36" fill="none" stroke="#fff" stroke-width="2"><rect x="4" y="16" width="32" height="14" rx="4"/><path d="M9 16l4-7h14l4 7"/><path d="M6 5l2 3M34 5l-2 3"/></svg></div>

<section class="abs reviews"></section>
<h2 class="heading" style="position:absolute;left:73px;top:2027px;font-size:44px">Customer Reviews</h2>
<div class="abs badge" aria-label="Review rating badge"><i></i></div>

<svg class="arrow" style="left:45px" width="16" height="28" fill="none" stroke="#fff" stroke-width="2.5"><path d="M14 2L3 14l11 12"/></svg>
<svg class="arrow" style="left:1142px" width="16" height="28" fill="none" stroke="#fff" stroke-width="2.5"><path d="M2 2l11 12L2 26"/></svg>

<article class="card" style="left:75px"><span class="avatar">H</span><h4>Name Heading</h4><span class="stars">★★★★★</span><p>Sed ut perspiciatis unde omnis iste natus error sit voluptatem accusantium doloremque laudantium..</p><time>05/12/2025</time></article>
<article class="card focus" style="left:438px"><span class="avatar">H</span><h4>Name Heading</h4><span class="stars">★★★★★</span><p>Sed ut perspiciatis unde omnis iste natus error sit voluptatem accusantium doloremque laudantium..</p><time>05/12/2025</time></article>
<article class="card" style="left:798px"><span class="avatar">H</span><h4>Name Heading</h4><span class="stars">★★★★★</span><p>Sed ut perspiciatis unde omnis iste natus error sit voluptatem accusantium doloremque laudantium..</p><time>05/12/2025</time></article>
<span class="btn" style="left:517px;top:2350px;width:166px;height:45px">View All Reviews</span>

<section class="abs gallery"></section>
<h2 class="section-title heading" style="top:2518px">Bright Peel Co Gallery</h2>
<div class="shot" style="left:75px;top:2605px;width:338px;height:215px;background:linear-gradient(135deg,#2a2a2c,#0e0e10 60%,#4a4a4c)" role="img" aria-label="Matte black car bonnet and grille"></div>
<div class="shot" style="left:431px;top:2605px;width:339px;height:215px;background:linear-gradient(135deg,#8a8e94,#b45a1e 50%,#2a2a2c)" role="img" aria-label="Orange coupe with black bonnet in snow"></div>
<div class="shot" style="left:787px;top:2605px;width:339px;height:215px;background:linear-gradient(135deg,#4a6a3a,#1a1c24 55%,#5a5a5c)" role="img" aria-label="Black SUV parked outdoors"></div>
<div class="shot" style="left:75px;top:2840px;width:248px;height:213px;background:linear-gradient(135deg,#3a3a3e,#7a1a1e 50%,#2a2a2a)" role="img" aria-label="Red car with black roof"></div>
<div class="shot" style="left:342px;top:2840px;width:248px;height:213px;background:linear-gradient(135deg,#5a5a5e,#c0201e 50%,#1a1a1a)" role="img" aria-label="Red hatchback with black stripes"></div>
<div class="shot" style="left:610px;top:2840px;width:248px;height:213px;background:linear-gradient(135deg,#5a5a60,#2e2e32 55%,#707074)" role="img" aria-label="Satin grey sedan front"></div>
<div class="shot" style="left:877px;top:2840px;width:249px;height:213px;background:linear-gradient(135deg,#7a8a6a,#3a4a2e 55%,#1a1a1a)" role="img" aria-label="Olive green muscle car"></div>

<section class="abs contact"></section>
<svg class="abs" style="left:75px;top:3210px" width="512" height="390" viewBox="0 0 512 390">
  <defs><linearGradient id="fb" x1="0" y1="0" x2="1" y2="0"><stop offset="0" stop-color="#7a3fdc"/><stop offset="1" stop-color="#1c9cf2"/></linearGradient></defs>
  <polygon points="0,0 512,0 478,23 18,23 18,368 0,388" fill="url(#fb)"/>
</svg>
<form class="abs form-box">
  <h2 class="heading">Contact Us</h2>
  <div class="field" style="left:17px;top:87px;width:270px;height:47px">Name</div>
  <div class="field" style="left:297px;top:87px;width:268px;height:47px">Email Address</div>
  <div class="field" style="left:17px;top:145px;width:270px;height:47px">Phone No</div>
  <div class="field" style="left:297px;top:145px;width:268px;height:47px">Subject</div>
  <div class="field" style="left:17px;top:203px;width:548px;height:95px">Message</div>
  <span class="btn btn-blue" style="left:17px;top:311px;width:141px;height:47px">Submit Now</span>
</form>

<div class="contact-info"><h2 class="heading">Contact Info</h2></div>
<div class="info" style="top:3315px"><span class="dot"><svg width="20" height="20" fill="#fff"><path d="M10 1a6 6 0 0 0-6 6c0 5 6 12 6 12s6-7 6-12a6 6 0 0 0-6-6zm0 8a2 2 0 1 1 0-4 2 2 0 0 1 0 4z"/></svg></span><h5>Address</h5><p>48 Harrow Lane Unit 12,<br>Calgary AB T2P 1J9, Canada</p></div>
<div class="info" style="top:3417px"><span class="dot"><svg width="20" height="20" fill="#fff"><path d="M5 2l3 4-2 2c1 3 3 5 6 6l2-2 4 3-2 3C9 18 2 11 2 4z"/></svg></span><h5>Phone</h5><p>+1-555-014-2270</p></div>
<div class="info" style="top:3495px"><span class="dot"><svg width="20" height="16" fill="#fff"><path d="M1 2h18v12H1z"/><path d="M1 2l9 7 9-7" stroke="#7a3fdc" stroke-width="1.5" fill="none"/></svg></span><h5>Email</h5><p>hello@brightpeel.example</p></div>
<span class="btn" style="left:742px;top:3570px;width:142px;height:47px;background:var(--blue)">Map Location</span>

<footer class="abs footer"></footer>
<div class="wordmark footer-mark" style="position:absolute;left:124px;top:3776px;font-size:28px"><i></i>Bright Peel Co</div>
<p class="copy">Copyright © 2025 Company Name<br>All Right Reserved</p>

<h6 style="position:absolute;top:3772px;left:355px;font-family:'Oswald',sans-serif;font-weight:500;font-size:20px">QUICK LINKS</h6>
<span class="flink" style="left:355px;top:3810px">Home</span>
<span class="flink" style="left:355px;top:3841px">About Us</span>
<span class="flink" style="left:355px;top:3872px">Services</span>
<span class="flink" style="left:355px;top:3903px">Gallery</span>
<span class="flink" style="left:458px;top:3810px">FAQ's</span>
<span class="flink" style="left:458px;top:3841px">Products</span>
<span class="flink" style="left:458px;top:3872px">Blog</span>
<span class="flink" style="left:458px;top:3903px">Contact</span>

<h6 style="position:absolute;top:3772px;left:596px;font-family:'Oswald',sans-serif;font-weight:500;font-size:20px">SERVICES</h6>
<span class="flink" style="left:596px;top:3810px">Vinyl Wraps</span>
<span class="flink" style="left:596px;top:3841px">Paint Protection Film</span>
<span class="flink" style="left:596px;top:3872px">Matte PPF</span>
<span class="flink" style="left:596px;top:3903px">Coloured PPF</span>
<span class="flink" style="left:773px;top:3810px">Window Tinting</span>
<span class="flink" style="left:773px;top:3841px">Detailing</span>
<span class="flink" style="left:773px;top:3872px">Custom Decals</span>

<h6 style="position:absolute;top:3772px;left:945px;font-family:'Oswald',sans-serif;font-weight:500;font-size:20px">FOLLOW US</h6>
<span class="social" style="left:945px"></span>
<span class="social" style="left:974px;background:var(--blue)"></span>
<span class="social" style="left:1012px"></span>
<span class="social" style="left:1052px"></span>
<span class="social" style="left:1094px"></span>

</body>
</html>
```